Business Card Design Project

we need a business card design for our company: www.plomvik.ch
It's important to include our already existing logo (see website)

```html
<!DOCTYPE html>
<html lang="en">
<head>
<meta charset="utf-8">
<title>Plomvik business card</title>
<link href="https://fonts.googleapis.com/css2?family=Exo+2:wght@300;400;500;600&display=swap" rel="stylesheet">
<style>
  :root {
    --stage: #e6e6e6;
    --card-black: #050505;
    --card-white: #ffffff;
    --brand-blue: #1a8cff;
    --accent-blue: #8fd0ff;
    --line-blue: #4aa8f0;
    --url-blue: #6db8f2;
    --ink: #111111;
    --muted: #a8a8a8;
  }
  * { margin: 0; padding: 0; box-sizing: border-box; }
  html, body { width: 1200px; height: 900px; overflow: hidden; background: var(--stage); }
  body { position: relative; font-family: "Exo 2", sans-serif; }

  .card {
    position: absolute;
    width: 700px;
    height: 400px;
    border-radius: 24px;
    overflow: hidden;
    background: var(--card-black);
  }
  .card-front { left: 32px; top: 32px; }
  .card-back { left: 466px; top: 466px; height: 398px; }

  .card-shape { position: absolute; inset: 0; width: 100%; height: 100%; }

  .brand-name {
    position: absolute;
    left: 52px; top: 84px;
    font-size: 72px;
    font-weight: 600;
    letter-spacing: -1px;
    color: var(--brand-blue);
    line-height: 1;
  }

  .company-block { position: absolute; left: 52px; top: 312px; color: var(--muted); }
  .company-name { font-size: 16px; font-weight: 600; }
  .company-address { font-size: 12.5px; font-weight: 400; margin-top: 4px; }

  .person {
    position: absolute;
    right: 28px; top: 40px;
    text-align: right;
    color: var(--ink);
  }
  .person-name { font-size: 30px; font-weight: 500; line-height: 1.1; }
  .person-role { font-size: 15px; font-weight: 400; margin-top: 2px; }

  .contact-list {
    position: absolute;
    left: 494px; top: 202px;
    list-style: none;
    color: var(--ink);
    font-size: 15px;
  }
  .contact-list li { display: flex; align-items: center; height: 26px; }
  .contact-list li.gap { margin-top: 20px; }
  .contact-icon { width: 16px; height: 16px; margin-right: 10px; flex: none; }

  .back-rule {
    position: absolute;
    left: 140px; top: 0;
    width: 3px; height: 100%;
    background: var(--line-blue);
  }
  .back-url {
    position: absolute;
    left: 290px; top: 170px;
    font-size: 36px;
    font-weight: 300;
    color: var(--url-blue);
    letter-spacing: 0.5px;
  }
</style>
</head>
<body>

<section class="card card-front">
  <svg class="card-shape" viewBox="0 0 700 400" aria-hidden="true">
    <path d="M454,0 C438,170 410,320 360,400 L700,400 L700,0 Z" fill="var(--accent-blue)"/>
    <path d="M456,0 C452,170 432,320 388,400 L700,400 L700,0 Z" fill="var(--card-white)"/>
  </svg>

  <div class="brand-name">Plomvik</div>

  <div class="company-block">
    <div class="company-name">Plomvik AG</div>
    <div class="company-address">Lindenweg 12 - 8005 Zürich</div>
  </div>

  <div class="person">
    <div class="person-name">Lukas Brenner</div>
    <div class="person-role">Manager</div>
  </div>

  <ul class="contact-list">
    <li>
      <svg class="contact-icon" viewBox="0 0 16 16" aria-hidden="true">
        <rect x="4" y="1" width="8" height="14" rx="1.5" fill="none" stroke="var(--line-blue)" stroke-width="1.5"/>
        <line x1="7" y1="12.5" x2="9" y2="12.5" stroke="var(--line-blue)" stroke-width="1.5"/>
      </svg>
      +41.79.612.4803
    </li>
    <li>
      <svg class="contact-icon" viewBox="0 0 16 16" aria-hidden="true">
        <path d="M3,1.5 L6,1.5 L7,5 L5.2,6.3 C6,8.2 7.8,10 9.7,10.8 L11,9 L14.5,10 L14.5,13 C14.5,14 13.5,14.7 12.5,14.5 C7,13.5 2.5,9 1.5,3.5 C1.3,2.5 2,1.5 3,1.5 Z" fill="var(--line-blue)"/>
      </svg>
      +41.44.287.9150
    </li>
    <li class="gap">
      <svg class="contact-icon" viewBox="0 0 16 16" aria-hidden="true">
        <rect x="1.5" y="3.5" width="13" height="9" fill="none" stroke="var(--line-blue)" stroke-width="1.4"/>
        <polyline points="1.5,3.5 8,9 14.5,3.5" fill="none" stroke="var(--line-blue)" stroke-width="1.4"/>
      </svg>
      info@plomvik.ch
    </li>
    <li>
      <svg class="contact-icon" viewBox="0 0 16 16" aria-hidden="true">
        <circle cx="8" cy="8" r="6.5" fill="none" stroke="var(--line-blue)" stroke-width="1.4"/>
        <ellipse cx="8" cy="8" rx="2.8" ry="6.5" fill="none" stroke="var(--line-blue)" stroke-width="1.2"/>
        <line x1="1.5" y1="8" x2="14.5" y2="8" stroke="var(--line-blue)" stroke-width="1.2"/>
      </svg>
      www.plomvik.ch
    </li>
  </ul>
</section>

<section class="card card-back">
  <div class="back-rule"></div>
  <div class="back-url">www.plomvik.ch</div>
</section>

</body>
</html>
```